New Website Design for Rides for Heroes.org - A Site for People to Donate Cars to War / Disabled Ve

Current site: www.ridesforheroes.org; Look at these sites for ideas: bikez2tots.org; gearsforhopes.org; www.autosformarines.org; www.trucksforsoldiers.org

Industry/Entity Type

Charity

Coding

Coded - Design and coding required

Number of Pages Required

1 page

Requirements
Must have
• n/a
Nice to have
• n/a
Should not have
• n/a

```html
<!DOCTYPE html>
<html lang="en">
<head>
<meta charset="utf-8">
<title>Rides for Heroes.org – Car Donation</title>
<link rel="stylesheet" href="https://fonts.googleapis.com/css2?family=Roboto:wght@300;400;500&display=swap">
<style>
:root{
  --sky:#8db4d9;
  --navy:#2b5679;
  --footer:#274b6d;
  --orange:#d47b34;
  --white:#ffffff;
  --hero-top:#4a6fb3;
  --hero-bottom:#6d8fca;
  --ink-blue:#4f79b5;
}
*{box-sizing:border-box;margin:0;padding:0}
html,body{width:1093px;height:1200px;overflow:hidden}
body{position:relative;background:var(--sky);font-family:'Roboto',sans-serif;color:var(--white);font-weight:300}
.abs{position:absolute}

.main-nav a{position:absolute;top:17px;height:39px;border-radius:6px;background:var(--navy);color:var(--white);
  font-size:12px;font-weight:400;text-decoration:none;display:flex;align-items:center;justify-content:center;text-transform:uppercase}
.main-nav a.is-active{background:var(--orange)}

.hero{left:57px;top:84px;width:983px;height:239px;background:linear-gradient(180deg,var(--hero-top),var(--hero-bottom))}
.hero-photo{position:absolute;left:450px;top:0;width:420px;height:239px;background:radial-gradient(ellipse at 50% 70%,#6b6a52 0%,#8a8a78 35%,rgba(109,143,202,0) 70%)}
.org-name{position:absolute;left:98px;top:92px;display:flex;align-items:center;gap:10px;font-size:24px;font-weight:400;color:var(--white)}
.org-name i{display:block;width:14px;height:14px;background:var(--white)}
.hero-arrow{position:absolute;top:200px}

.campaign-bar{left:57px;top:323px;width:983px;height:50px;display:flex}
.campaign-join{width:482px;background:var(--orange);position:relative}
.campaign-join .join{position:absolute;left:103px;top:10px;font-size:13.5px;font-weight:400;line-height:1.25}
.campaign-join .cta{position:absolute;left:276px;top:10px;font-size:23px;font-weight:300}
.campaign-total{flex:1;background:var(--white);color:var(--ink-blue);font-size:23px;display:flex;align-items:center;justify-content:center}
.campaign-total em{font-style:normal;color:var(--orange);margin-left:6px}

.info-col{top:435px;width:192px}
.info-col h3{font-size:17px;font-weight:400;line-height:1.3;margin-bottom:14px}
.info-col p{font-size:13.5px;line-height:1.34}

.read-more{top:664px;width:212px;height:50px;display:flex;text-decoration:none;color:var(--white)}
.read-more .label{flex:1;background:var(--navy);font-size:24px;font-weight:300;display:flex;align-items:center;padding-left:17px}
.read-more .go{width:67px;background:var(--orange);display:flex;align-items:center;justify-content:center}

.feature-photo{top:741px;height:177px}
.photo-gift{left:57px;width:212px;background:linear-gradient(135deg,#e4ecf2,#b9c9d6)}
.photo-keys{left:298px;width:213px;background:linear-gradient(135deg,#2d3b4c,#5b6f82 55%,#7a4c4a)}

.program{left:558px;top:435px;width:460px}
.program h1{font-size:29px;font-weight:400;line-height:1.2;margin-bottom:36px}
.program h2{font-size:17px;font-weight:400;line-height:1.3;margin-bottom:14px}
.program p{font-size:13.5px;line-height:1.34;margin-bottom:17px}

.site-footer{left:0;top:986px;width:1093px;height:214px;background:var(--footer)}
.footer-col{position:absolute;top:38px}
.footer-col h4{font-size:21px;font-weight:400;display:inline-block;padding-bottom:4px;border-bottom:2px solid var(--orange);margin-bottom:14px}
.footer-col p{font-size:11.5px;font-weight:400;line-height:1.4}
.phone{font-size:23px;font-weight:400;text-align:center;margin-bottom:18px}
.social{display:flex;gap:18px;justify-content:center}
.social span{width:48px;height:48px;display:block}
.social .s1{background:#3b5a93}.social .s2{background:#2fa7db}.social .s3{background:#ef7f35}.social .s4{background:#c9392d}
</style>
</head>
<body>

<nav class="main-nav">
  <a class="is-active" href="#" style="left:206px;width:137px">Home</a>
  <a href="#" style="left:345px;width:140px">About</a>
  <a href="#" style="left:487px;width:235px">Why donate your car</a>
  <a href="#" style="left:724px;width:278px">How to donate your vehicle</a>
</nav>

<section class="hero abs">
  <div class="hero-photo" role="img" aria-label="Photo of a soldier embracing a child holding a small flag"></div>
  <div class="org-name"><i></i>Valor Lane Charity</div>
  <svg class="hero-arrow" style="left:66px" width="16" height="26" viewBox="0 0 16 26"><path d="M13 2 3 13l10 11" fill="none" stroke="#fff" stroke-width="3"/></svg>
  <svg class="hero-arrow" style="left:900px" width="16" height="26" viewBox="0 0 16 26"><path d="M3 2l10 11L3 24" fill="none" stroke="#fff" stroke-width="3"/></svg>
</section>

<div class="campaign-bar abs">
  <div class="campaign-join">
    <div class="join">JOIN OUR<br>CAMPAIGN</div>
    <div class="cta">Donate now! &gt;</div>
  </div>
  <div class="campaign-total">Donate so far <em>$600 000</em></div>
</div>

<section class="info-col abs" style="left:64px">
  <h3>HOW IT WORKS</h3>
  <p>We guide you through the process - it is fast and easy! We'll call you to arrange a free pickup time.<br>The driver will help you with all paperwork and issue you with a pickup receipt for your records.<br>We get the highest value for your donation.</p>
</section>

<section class="info-col abs" style="left:315px">
  <h3>DONATE YOUR CAR<br>TODAY!</h3>
  <p>1. Free up space in your garage. Avoid the hassles of selling your car.<br>2. No need to pay hefty car repair bills.<br>3. You're helping a soldier or veteran in need.<br>5. Turn that unwanted car into an IRS tax deduction</p>
</section>

<a class="read-more abs" href="#" style="left:57px"><span class="label">Read more</span><span class="go"><svg width="14" height="22" viewBox="0 0 14 22"><path d="M3 2l8 9-8 9" fill="none" stroke="#fff" stroke-width="3"/></svg></span></a>
<a class="read-more abs" href="#" style="left:299px"><span class="label">Read more</span><span class="go"><svg width="14" height="22" viewBox="0 0 14 22"><path d="M3 2l8 9-8 9" fill="none" stroke="#fff" stroke-width="3"/></svg></span></a>

<div class="feature-photo photo-gift abs" role="img" aria-label="Photo of hands holding a small model car wrapped in a red ribbon"></div>
<div class="feature-photo photo-keys abs" role="img" aria-label="Photo of a handshake with car keys being handed over"></div>

<section class="program abs">
  <h1>CHARITY CAR DONATION PROGRAM HELPING VETERANS AND OUR MILITARY</h1>
  <h2>MAKE A CAR DONATION TODAY &amp; HELP THE MILITARY CHARITY OF YOUR CHOICE!</h2>
  <p>RidesForHeroes is the nation's premier vehicle donation program that supports our American heroes and their families.</p>
  <p>Our main goal is to improve the lives of as many of our military and veterans as possible by uniting dozens of supporting foundations under one unique program.</p>
  <p>Each charity offers different services relating to veterans, the military and their families and survivors. By giving, everyone can feel good about giving back to these heroes!</p>
  <p>Our donation program allows you the donor to select the military or veterans charity you feel most passionate about.</p>
</section>

<footer class="site-footer abs">
  <div class="footer-col" style="left:57px;width:280px">
    <h4>CONTACT INFORMATION</h4>
    <p>For immediate scheduling of your vehicle donation, please call 1-800-555-0142. Experienced representatives are available anytime day or night to assist you with the entire transaction.</p>
  </div>
  <div class="footer-col" style="left:401px;width:270px">
    <h4>WE ARE A NON-PROFIT</h4>
    <p>Trucks for Soldiers is Auto Giving Foundation's vehicle donation program. Auto Giving Foundation is a tax exempt charity under section 501(c)(3) of the IRS Code. Auto Giving Foundation donates proceeds from its Trucks for Soldiers program to other tax exempt charities that help disabled veterans.</p>
  </div>
  <div class="footer-col" style="left:740px;width:246px;text-align:center">
    <h4>CONNECT WITH US</h4>
    <div class="phone">1-800-555-0142</div>
    <div class="social">
      <span class="s1" role="img" aria-label="Social link"></span>
      <span class="s2" role="img" aria-label="Social link"></span>
      <span class="s3" role="img" aria-label="News feed link"></span>
      <span class="s4" role="img" aria-label="Social link"></span>
    </div>
  </div>
</footer>

</body>
</html>
```